HomeBridle business card and stationary design

We are looking for a simple yet elegant design for our mortgage company business card and stationary.

The card should include:
Name (Derek Walsh)
Title (CEO)
Phone Number (614-208-3917)
Address (48 Birchfield Court, Suite 314, Marlow, OH 43952)
Email (email@homebridle-example.com)
"NMLS" i.e. (NMLS 61947)
"Company NMLS" (Company NMLS 472815)

See above

```html
<!DOCTYPE html>
<html lang="en">
<head>
<meta charset="utf-8">
<title>HomeBridle Business Card</title>
<link href="https://fonts.googleapis.com/css2?family=Montserrat:wght@400;500;600;700&display=swap" rel="stylesheet">
<style>
  :root {
    --backdrop: #3b3b3c;
    --card: #1c1c1d;
    --accent: #1fa6e8;
    --text: #f2f2f2;
    --muted: #cfcfcf;
    --emboss: #8c8c8e;
  }
  * { box-sizing: border-box; margin: 0; padding: 0; }
  html, body {
    width: 1200px; height: 801px; overflow: hidden;
    background: var(--backdrop);
    font-family: "Montserrat", sans-serif;
  }
  .stage {
    position: relative; width: 1200px; height: 801px;
  }
  .card {
    position: absolute; width: 525px; height: 300px;
    background: var(--card);
    border-bottom: 3px solid var(--accent);
    box-shadow: 0 12px 30px rgba(0,0,0,0.45);
    overflow: hidden;
  }
  .card--front { left: 50px; top: 250px; }
  .card--back { left: 625px; top: 250px; }

  .brand-name {
    position: absolute; left: 38px; top: 88px;
    font-size: 40px; font-weight: 600; letter-spacing: -0.5px;
    color: var(--text);
  }
  .divider {
    position: absolute; left: 0; right: 0; top: 172px;
    height: 1px; background: var(--accent);
  }
  .person {
    position: absolute; right: 34px; top: 120px; text-align: right;
  }
  .person__name {
    font-size: 20px; font-weight: 700; letter-spacing: 0.5px;
    color: var(--accent); text-transform: uppercase;
  }
  .person__title {
    font-size: 11px; font-weight: 500; color: var(--text); margin-top: 2px;
  }
  .address {
    position: absolute; right: 34px; top: 186px; text-align: right;
    font-size: 12px; line-height: 1.5; color: var(--text);
  }
  .contacts {
    position: absolute; left: 38px; top: 196px; list-style: none;
    font-size: 12px; line-height: 1; color: var(--text);
  }
  .contacts li {
    display: flex; align-items: center; gap: 8px; margin-bottom: 9px;
  }
  .contacts svg { width: 11px; height: 11px; fill: var(--accent); flex: none; }

  .brand-mark {
    position: absolute; left: 0; right: 0; top: 96px; text-align: center;
    font-size: 56px; font-weight: 600; letter-spacing: -1px;
    color: var(--emboss);
  }
  .licenses {
    position: absolute; left: 0; right: 0; bottom: 38px; text-align: center;
    font-size: 13px; color: var(--text); letter-spacing: 0.3px;
  }
  .licenses .sep { color: var(--accent); margin: 0 8px; }
</style>
</head>
<body>
<main class="stage">
  <section class="card card--front">
    <div class="brand-name">HomeBridle</div>
    <div class="person">
      <div class="person__name">Derek Walsh</div>
      <div class="person__title">CEO</div>
    </div>
    <div class="divider"></div>
    <address class="address">
      48 Birchfield Court, Suite 314<br>
      Marlow, OH 43952
    </address>
    <ul class="contacts">
      <li>
        <svg viewBox="0 0 24 24" aria-hidden="true"><path d="M6.6 10.8a15.1 15.1 0 0 0 6.6 6.6l2.2-2.2c.3-.3.7-.4 1-.2 1.1.4 2.3.6 3.6.6.6 0 1 .4 1 1V20c0 .6-.4 1-1 1A17 17 0 0 1 3 4c0-.6.4-1 1-1h3.5c.6 0 1 .4 1 1 0 1.3.2 2.5.6 3.6.1.3 0 .7-.2 1z"/></svg>
        614-208-3917
      </li>
      <li>
        <svg viewBox="0 0 24 24" aria-hidden="true"><path d="M2 5h20v14H2zM4 7v.5l8 5 8-5V7l-8 5z"/></svg>
        email@homebridle-example.com
      </li>
      <li>
        <svg viewBox="0 0 24 24" aria-hidden="true"><path d="M12 2a10 10 0 1 0 0 20 10 10 0 0 0 0-20zm6.9 6h-2.9a15 15 0 0 0-1.3-3.6A8 8 0 0 1 18.9 8zM12 4c.8 1.2 1.5 2.5 1.9 4h-3.8c.4-1.5 1.1-2.8 1.9-4zM4.3 14a8 8 0 0 1 0-4h3.4a16 16 0 0 0 0 4zm.8 2h2.9c.3 1.3.8 2.5 1.4 3.6A8 8 0 0 1 5.1 16zM8 8H5.1a8 8 0 0 1 4.3-3.6C8.8 5.5 8.3 6.7 8 8zm4 12c-.8-1.2-1.5-2.5-1.9-4h3.8c-.4 1.5-1.1 2.8-1.9 4zm2.3-6H9.7a14 14 0 0 1 0-4h4.6a14 14 0 0 1 0 4zm.3 5.6c.6-1.1 1.1-2.3 1.4-3.6h2.9a8 8 0 0 1-4.3 3.6zm1.7-5.6a16 16 0 0 0 0-4h3.4a8 8 0 0 1 0 4z"/></svg>
        www.homebridle.com
      </li>
    </ul>
  </section>

  <section class="card card--back">
    <div class="brand-mark">HomeBridle</div>
    <p class="licenses">NMLS 61947<span class="sep">•</span>Company NMLS 472815</p>
  </section>
</main>
</body>
</html>
```